Design of a graphic project for an advertisement on construction site barriers

Design of a graphic project for a staircase manufacturing company, intended to be printed on large format construction site barriers
(340cm x 173cm)

Information to display:
-the complete logo (the one with the text "original staircase" without retouching it, in horizontal or centered version, free choice)
-Tel: 0468 219 835
-Mail: info@vkr7.be
-Web: vkr7.be
-Write the text: “Stair creator” (IN FRENCH PLEASE!!!)
-Display the different logos of social networks: Facebook, Instagram, TikTok, YouTube
-the QR code (pay attention to the quality of the interior logo, it is too weak, it must be redone with the logo attached)
-Choose a few photos in the link that will best suit your design,
https://albums.example-pics.be/Tn4wRzq8LmYd2Hs
I would like an attractive, professional, beautiful, modern design, worthy of a large company to display prominently on my construction sites.

Pay attention to the quality of the graphic as it will be printed large on a measurement of 340cm by 173cm

Target Market(s)

customer for the construction of a staircase

Industry/Entity Type

créateur d'escalier

Requirements
Must have
• everything is said in the description
Nice to have
• On a black background, I prefer the white version of the logos
Should not have
• Do not add photos of other stairs found on the internet, only photos from the Google link given in the description

```html
<!DOCTYPE html>
<html lang="fr">
<head>
<meta charset="utf-8">
<title>VKR7 – Créateur d'escalier</title>
<link href="https://fonts.googleapis.com/css2?family=Montserrat:wght@400;500;600&display=swap" rel="stylesheet">
<style>
  :root {
    --page: #e9ecef;
    --panel: #2b2624;
    --ink: #ffffff;
    --accent: #7fa6c8;
    --photo-light: #d9d8d3;
    --photo-mid: #b9b8b2;
    --photo-dark: #6f6e6a;
  }
  * { margin: 0; padding: 0; box-sizing: border-box; }
  html, body { width: 1200px; height: 800px; overflow: hidden; background: var(--page); }
  body { font-family: "Montserrat", sans-serif; color: var(--ink); }

  .barrier {
    position: absolute;
    left: 0; top: 95px;
    width: 1200px; height: 610px;
    background: var(--panel);
    overflow: hidden;
  }

  .brand {
    position: absolute;
    left: 290px; top: 40px;
    display: flex;
    align-items: center;
    gap: 60px;
  }
  .brand-square {
    width: 96px; height: 96px;
    background: var(--accent);
    flex: none;
  }
  .brand-name {
    font-size: 128px;
    font-weight: 400;
    letter-spacing: 6px;
    line-height: 1;
    color: var(--ink);
  }

  .staircase-photo {
    position: absolute;
    left: 484px; top: 196px;
    width: 716px; height: 414px;
    background: linear-gradient(135deg, var(--photo-light) 0%, var(--photo-mid) 55%, var(--photo-dark) 100%);
  }

  .tagline {
    position: absolute;
    left: 104px; top: 320px;
    width: 350px;
    text-align: right;
    font-size: 26px;
    font-weight: 600;
    letter-spacing: 0.5px;
    text-transform: uppercase;
    white-space: nowrap;
  }

  .contacts {
    position: absolute;
    left: 58px; top: 410px;
    list-style: none;
  }
  .contacts li {
    display: flex;
    align-items: center;
    height: 62px;
    font-size: 29px;
    font-weight: 500;
    white-space: nowrap;
  }
  .contacts .icon {
    width: 42px; height: 42px;
    margin-right: 30px;
    flex: none;
  }
  .contacts .phone { font-weight: 600; letter-spacing: 1px; }
</style>
</head>
<body>
  <section class="barrier">
    <div class="brand">
      <div class="brand-square"></div>
      <div class="brand-name">VKR7</div>
    </div>

    <div class="staircase-photo" role="img" aria-label="Photo of a white floating staircase in a bright, minimal interior"></div>

    <p class="tagline">Créateur d'escalier</p>

    <ul class="contacts">
      <li>
        <svg class="icon" viewBox="0 0 42 42" aria-hidden="true">
          <circle cx="21" cy="21" r="19" fill="none" stroke="#fff" stroke-width="2.5"/>
          <rect x="14.5" y="10" width="13" height="22" rx="2" fill="none" stroke="#fff" stroke-width="2"/>
          <line x1="19" y1="28.5" x2="23" y2="28.5" stroke="#fff" stroke-width="2"/>
        </svg>
        <span class="phone">0468 219 835</span>
      </li>
      <li>
        <svg class="icon" viewBox="0 0 42 42" aria-hidden="true">
          <circle cx="21" cy="21" r="19" fill="none" stroke="#fff" stroke-width="2.5"/>
          <rect x="11" y="14" width="20" height="14" fill="none" stroke="#fff" stroke-width="2"/>
          <polyline points="11,14 21,22 31,14" fill="none" stroke="#fff" stroke-width="2"/>
        </svg>
        <span>info@vkr7.be</span>
      </li>
      <li>
        <svg class="icon" viewBox="0 0 42 42" aria-hidden="true">
          <circle cx="21" cy="21" r="19" fill="none" stroke="#fff" stroke-width="2.5"/>
          <circle cx="21" cy="21" r="11" fill="none" stroke="#fff" stroke-width="2"/>
          <ellipse cx="21" cy="21" rx="5" ry="11" fill="none" stroke="#fff" stroke-width="1.8"/>
          <line x1="10" y1="21" x2="32" y2="21" stroke="#fff" stroke-width="1.8"/>
          <line x1="12" y1="15.5" x2="30" y2="15.5" stroke="#fff" stroke-width="1.5"/>
          <line x1="12" y1="26.5" x2="30" y2="26.5" stroke="#fff" stroke-width="1.5"/>
        </svg>
        <span>vkr7.be</span>
      </li>
    </ul>
  </section>
</body>
</html>
```